Marketing Flyer for Plumber Referals

8.5" x11" Layout should be landscape not portrait. Create a bold, eye-catching flyer that highlights earning potential from referrals for water damage restoration. Use high-contrast colors like blue, yellow, and white, with bold fonts and dynamic layouts. Include images of restoration work, cash, and happy clients. Emphasize key benefits like $500 minimum payouts, fast payments, and unlimited income potential. Keep instructions simple: refer a client, we handle the work, you get paid. Add a clear call-to-action and display contact details prominently. Focus on professionalism and energy.

Target Market(s)

Plumbers and Contractor 8.5" x11" Layout should be landscape not portrait.

Industry/Entity Type

General Contractor

Colors
0054AA
0677BA
7BADD7
CADEEF
E8F1F8
EB3D1F
EC4F4E
F09395
F8D3D4
FCEDEE

Requirements
Must have
• 8.5" x11" Layout should be landscape not portrait.
Nice to have

```html
<!DOCTYPE html>
<html lang="en">
<head>
<meta charset="utf-8">
<title>Get Paid to Refer a Flood – Referral Flyer</title>
<link rel="stylesheet" href="https://fonts.googleapis.com/css2?family=Oswald:wght@500;600;700&family=Poppins:wght@400;600;700;800&display=swap">
<style>
  :root {
    --stage: #3b3e43;
    --red-dark: #a9282b;
    --red: #ec4f4e;
    --red-band: #c8312f;
    --blue: #1547a0;
    --blue-deep: #0f3a8c;
    --concrete: #cfcfcf;
    --concrete-light: #e2e2e2;
    --white: #ffffff;
  }
  * { box-sizing: border-box; margin: 0; padding: 0; }
  html, body { width: 856px; height: 1200px; overflow: hidden; }
  body {
    background: var(--stage);
    position: relative;
    font-family: "Poppins", sans-serif;
    color: var(--white);
  }
  .card {
    position: absolute;
    left: 69px;
    width: 727px;
    height: 562px;
    overflow: hidden;
    background: var(--blue);
    box-shadow: 0 4px 14px rgba(0,0,0,.45);
  }
  .card--front { top: 38px; }
  .card--back { top: 610px; }

  .concrete {
    position: absolute;
    background: radial-gradient(circle at 30% 40%, var(--concrete-light), var(--concrete) 70%);
  }
  .blue-field {
    position: absolute;
    background: radial-gradient(ellipse at 40% 50%, var(--blue), var(--blue-deep) 90%);
  }
  .headline-band {
    position: absolute;
    background: var(--red-dark);
    display: flex;
    align-items: center;
    justify-content: center;
    font-family: "Oswald", sans-serif;
    font-weight: 600;
    text-transform: uppercase;
    letter-spacing: .5px;
    color: var(--white);
    white-space: nowrap;
  }
  .tab {
    position: absolute;
    height: 64px;
    display: flex;
    align-items: center;
    justify-content: center;
    font-family: "Oswald", sans-serif;
    font-weight: 700;
    font-style: italic;
    color: var(--white);
    white-space: nowrap;
  }
  .tab svg { position: absolute; inset: 0; width: 100%; height: 100%; }
  .tab span { position: relative; }
  .photo { position: absolute; }

  /* Front */
  .front-photo {
    left: 0; top: 0; width: 322px; height: 562px;
    background: linear-gradient(160deg, #d9d8cf 0%, #b9bcb0 40%, #7fb3c4 55%, #2f55a8 80%, #24448e 100%);
  }
  .front-concrete { left: 322px; top: 0; width: 405px; height: 70px; }
  .front-headline { left: 322px; top: 70px; width: 405px; height: 84px; font-size: 31px; padding-left: 8px; }
  .front-blue { left: 322px; top: 154px; width: 405px; height: 352px; }
  .front-tab { left: 378px; top: 154px; width: 318px; font-size: 31px; }
  .steps { position: absolute; left: 347px; top: 259px; width: 360px; list-style: none; }
  .step { display: flex; gap: 12px; margin-bottom: 28px; }
  .step__num { font-weight: 800; font-size: 38px; line-height: 36px; width: 50px; flex: none; }
  .step__title { font-weight: 700; font-size: 14.5px; line-height: 18px; white-space: nowrap; }
  .step__text { font-size: 14px; line-height: 19.5px; padding-left: 20px; position: relative; margin-top: 1px; width: 286px; }
  .step__text::before { content: "•"; position: absolute; left: 7px; font-size: 11px; }
  .contact-band {
    position: absolute; left: 322px; top: 506px; width: 405px; height: 56px;
    background: var(--red-band);
    display: flex; align-items: center; justify-content: flex-end; gap: 24px;
    padding-right: 24px;
    font-family: "Oswald", sans-serif; font-weight: 600; font-size: 19px;
    white-space: nowrap;
  }
  .contact-band .phone { display: flex; align-items: center; gap: 5px; font-size: 21px; }

  /* Back */
  .back-concrete { left: 0; top: 0; width: 411px; height: 70px; }
  .brand {
    position: absolute; left: 0; top: 0; width: 411px; height: 70px;
    display: flex; align-items: center; justify-content: center;
    font-family: "Poppins", sans-serif; font-weight: 600; font-size: 10px;
    letter-spacing: 1.5px; color: #333;
  }
  .back-headline { left: 0; top: 70px; width: 411px; height: 84px; font-size: 35px; }
  .back-blue { left: 0; top: 154px; width: 727px; height: 408px; }
  .back-photo {
    left: 411px; top: 0; width: 316px; height: 440px;
    background: linear-gradient(180deg, #e8e6e1 0%, #cfc7b8 45%, #8e8775 75%, #5d5848 100%);
    border-bottom-left-radius: 140px 120px;
  }
  .back-person {
    left: 565px; top: 440px; width: 162px; height: 122px;
    background: linear-gradient(180deg, #6b4a38 0%, #d9382f 60%, #e2403a 100%);
    border-top-left-radius: 60px;
  }
  .back-tab { left: 42px; top: 154px; width: 312px; font-size: 21px; }
  .benefits-title { position: absolute; left: 36px; top: 236px; font-weight: 800; font-size: 20px; }
  .benefits { position: absolute; left: 41px; top: 266px; width: 320px; list-style: none; font-size: 13.5px; line-height: 18.2px; }
  .benefits b { font-weight: 700; }
  .promo-box {
    position: absolute; left: 0; top: 433px; width: 397px; height: 72px;
    background: var(--red-band);
    display: flex; align-items: center; padding-left: 36px; gap: 28px;
    font-family: "Oswald", sans-serif; font-weight: 600; font-size: 14px; line-height: 16.5px;
  }
  .promo { display: flex; align-items: center; gap: 12px; }
  .tagline {
    position: absolute; left: 26px; top: 517px;
    font-family: "Oswald", sans-serif; font-weight: 700; font-size: 21px; letter-spacing: .1px;
    white-space: nowrap;
  }
</style>
</head>
<body>

<section class="card card--front">
  <div class="photo front-photo" role="img" aria-label="Photo of hundred dollar bills with letter tiles spelling CASH FLOW and a smiling plumber in blue coveralls holding a wrench"></div>
  <div class="concrete front-concrete"></div>
  <h1 class="headline-band front-headline">Get Paid to Refer a Flood</h1>
  <div class="blue-field front-blue"></div>
  <div class="tab front-tab">
    <svg viewBox="0 0 318 64" preserveAspectRatio="none"><path d="M0 0 H318 L290 50 Q282 64 264 64 H54 Q36 64 28 50 Z" fill="#ec4f4e"/></svg>
    <span>How It Works</span>
  </div>
  <ol class="steps">
    <li class="step">
      <div class="step__num">01</div>
      <div><div class="step__title">Refer Flood, Water and Mold Damage</div>
      <div class="step__text">Call, book online, or text us directly.</div></div>
    </li>
    <li class="step">
      <div class="step__num">02</div>
      <div><div class="step__title">We Take Care of Everything</div>
      <div class="step__text">Free evaluations, insurance claims, and professional service.</div></div>
    </li>
    <li class="step">
      <div class="step__num">03</div>
      <div><div class="step__title">Get Paid Fast</div>
      <div class="step__text">$500 minimum or 10% of the invoice within 48 hours of final payment.</div></div>
    </li>
  </ol>
  <div class="contact-band">
    <span class="web">HARBORLINEREMODEL.COM</span>
    <span class="phone">
      <svg width="18" height="18" viewBox="0 0 20 20"><circle cx="10" cy="10" r="9" fill="none" stroke="#fff" stroke-width="2"/><path d="M6.5 5.5 L8.5 5.2 L9.3 7.8 L8.2 8.7 Q9.2 10.9 11.3 11.8 L12.2 10.7 L14.8 11.5 L14.5 13.5 Q9.5 14.2 6.5 8.5 Z" fill="#fff"/></svg>
      555-014-2290
    </span>
  </div>
</section>

<section class="card card--back">
  <div class="blue-field back-blue"></div>
  <div class="photo back-photo" role="img" aria-label="Photo of a flooded home interior with a staircase and a leaking white drain pipe"></div>
  <div class="photo back-person" role="img" aria-label="Photo of a man in a red t-shirt looking upward"></div>
  <div class="concrete back-concrete"></div>
  <div class="brand">HARBORLINE REMODEL</div>
  <h1 class="headline-band back-headline">Earn Unlimited Cash</h1>
  <div class="tab back-tab">
    <svg viewBox="0 0 312 64" preserveAspectRatio="none"><path d="M0 0 H312 L284 50 Q276 64 258 64 H54 Q36 64 28 50 Z" fill="#ec4f4e"/></svg>
    <span>GET PAID TO REFER A FLOOD</span>
  </div>
  <h2 class="benefits-title">Why Partner with Us?</h2>
  <ul class="benefits">
    <li><b>Guaranteed Payout:</b> Minimum $500 or 10% of the invoice, paid fast.</li>
    <li><b>Free Evaluations:</b> We assess damage and process insurance claims for your clients.</li>
    <li><b>Industry Leaders:</b> Certified experts with 24/7 rapid response.</li>
    <li><b>Affordable Solutions:</b> Lowest out-of-pocket costs for your customers.</li>
  </ul>
  <div class="promo-box">
    <div class="promo">
      <svg width="20" height="20" viewBox="0 0 20 20" fill="none" stroke="#fff" stroke-width="1.6" stroke-linejoin="round"><rect x="1.5" y="8.5" width="4" height="9.5"/><path d="M5.5 9 L9 2.5 Q11 2.5 11 4.5 L10.5 8 H16.5 Q18.5 8.2 18 10.3 L16.6 16.3 Q16.2 18 14.5 18 H5.5"/></svg>
      <span>$500 Minimum<br>or 10% Per Referral!</span>
    </div>
    <div class="promo">
      <svg width="20" height="20" viewBox="0 0 20 20" fill="none" stroke="#fff" stroke-width="1.6" stroke-linejoin="round"><rect x="1.5" y="8.5" width="4" height="9.5"/><path d="M5.5 9 L9 2.5 Q11 2.5 11 4.5 L10.5 8 H16.5 Q18.5 8.2 18 10.3 L16.6 16.3 Q16.2 18 14.5 18 H5.5"/></svg>
      <span>Partner with the<br>#1 Water Damage<br>Restoration Team</span>
    </div>
  </div>
  <p class="tagline">SEND REFERRALS. GET PAID. GROW YOUR BUSINESS</p>
</section>

</body>
</html>
```